i NEED A MY CURRENT LOGO UPDATED TO MAKE IT LOOK MORE MODERN. I WANT TO KEEP MY CURRENT COLOURS FOR THE LOGO WHICH ARE GREEN, BLACK, WHITE AND SILVER/METALIC COLOURS.

I RUN A BUSINESS WHICH IS CALLED "CONVEYANCING" IN AUSTRALIA. THIS BUSINESS PROVIDES A SERVICES FOR PEOPLE WHO ARE BUYING OR SELLING OR TRANSFER THEIR PROPERTY. WE ARE NOT A REAL ESTATE AGENT. WE PREPARE AND DO ALL WORK NECESSARY TO COMPLETE A LEGAL TRANSFER OF PROPERTY FOR CUSTOMERS. THE REASON i CHOSE THE NAME "ORTELL CONVEYANCING" IS BECAUSE WE CAN ONLY DO VICTORIAN PROPERTY TRANSFERS AND IN AUSTRALIA THE LAND IS TRANSFERED TO AN OWNER AND WHATEVER IS ON THE LAND BECOMES THE OWNERS.

MY LOGO MUST HAVE THE VICTORIAN STATE AS A SYMBOL (VICTORIA IS ONE OF THE STATES IN AUSTRALIA AND IT'S KNOWN AS A GREEN STATE). I CAN EMAIL YOU THE CURRENT LOGO TO GIVE YOU AN IDEA.

I'M HAPPY WITH THE CURRENT COLOURS BUT NOT THE LAYOUT OR DESIGN. AT THE MOMENT IT'S PRETTY PLAIN AND BORING.
Updates

Example - This is a creative design I copied from the net.

Hi All, I've posted a design in which I would like you to consider being creative with the victorian logo as they have done with the swan here.  Just an idea.

Hi All, I just wanted to let you know that other than the colours I requested I want you all to come up with your own idea of the logo.  So far this is the only create design I've seen. 

Target Market(s)

People that are in the market to buy or selling property/real estate.

Industry/Entity Type

Business

Requirements
Must have
• THE COLOURS MUST REMAIN THE SAME AND MUST BE PROFESSIONAL AS WE ARE A PART OF THE LEGAL (PROFESSIONAL)INDUSTRY IN AUSTRALIA
Nice to have
• MUST HAVE THE VICTORIAN LOGO/SYMBOL
Should not have
• SHOULD NOT BE BORING. THE DETAILS OF OUR ADDRESS ON THE ATTACHED IS OLD DETAILS NOT OUR CURRENT DETAILS. IT'S ATTACHED TO SHOW YOU AN EXAMPLE OF THE CURRENT LOGO.

```html
<!DOCTYPE html>
<html lang="en">
<head>
<meta charset="utf-8">
<title>Ortell Conveyancing – Identity Sheet</title>
<link rel="stylesheet" href="https://fonts.googleapis.com/css2?family=Open+Sans:wght@400;600;700&display=swap">
<style>
:root{
  --green:#4c8f1f;
  --green-dark:#1f5c14;
  --green-mid:#2f7a1c;
  --green-light:#6fb52c;
  --lime:#a8e04a;
  --black:#000;
  --ink:#222;
  --silver:#c9cbcc;
  --silver-light:#eceded;
  --grey:#666;
  --white:#fff;
}
*{box-sizing:border-box;margin:0;padding:0}
html,body{width:1200px;height:899px;overflow:hidden;background:var(--white)}
body{position:relative;font-family:"Open Sans",Arial,sans-serif;color:var(--ink)}

/* Logo lockup */
.lockup{position:absolute;display:flex;align-items:center;gap:14px}
.lockup .dot{border-radius:50%;flex:none}
.lockup .name{font-weight:600;line-height:1;display:flex;flex-direction:column}
.lockup .name .top{letter-spacing:-.5px}
.lockup .name .sub{letter-spacing:.5px;margin-top:4px}

.panel{position:absolute;left:13px;width:417px;height:204px}
.panel-white{top:10px;border:1px solid #555;background:var(--white)}
.panel-black{top:228px;background:var(--black)}

.lockup-lg{left:46px;top:50px}
.lockup-lg .dot{width:96px;height:96px}
.lockup-lg .name .top{font-size:58px}
.lockup-lg .name .sub{font-size:25px}

.on-white .dot{background:var(--green)}
.on-white .name{color:var(--green)}
.on-black .dot{background:var(--green-light)}
.on-black .name{color:var(--silver)}
.mono .dot{background:var(--black)}
.mono .name{color:var(--black)}

.mono{left:60px;top:455px}
.mono .dot{width:86px;height:86px}
.mono .name .top{font-size:50px;font-weight:700}
.mono .name .sub{font-size:22px;font-weight:700}
.mono .name{font-weight:700}

.symbol-mark{position:absolute;left:86px;top:638px;width:200px;height:178px;border-radius:50%;background:var(--green)}

/* Cards */
.card{position:absolute;width:329px;height:196px;border-radius:12px;overflow:hidden;box-shadow:0 0 0 1px #bbb}
.c1{left:481px;top:113px;background:var(--white)}
.c2{left:844px;top:113px}
.c3{left:481px;top:355px}
.c4{left:844px;top:355px}
.c5{left:481px;top:584px}
.c6{left:844px;top:584px}

.fill-green{background:radial-gradient(ellipse at 50% 35%,var(--green-light) 0%,var(--green-mid) 45%,var(--green-dark) 100%)}
.top-black{position:absolute;left:0;top:0;width:100%;background:var(--black)}
.bottom-green{position:absolute;left:0;bottom:0;width:100%;background:linear-gradient(180deg,var(--green-light),var(--green-dark))}

.card .lockup{gap:9px}
.card .lockup .dot{width:34px;height:34px}
.card .lockup .name .top{font-size:31px}
.card .lockup .name .sub{font-size:13px;margin-top:2px}
.on-green .dot{background:var(--white)}
.on-green .name{color:var(--white)}

.url-strip{position:absolute;left:0;width:100%;height:15px;font-size:9px;font-weight:700;text-align:center;line-height:15px}
.strip-black{background:var(--black);color:var(--white)}
.strip-black.lime{color:var(--lime)}
.strip-silver{background:linear-gradient(180deg,var(--silver-light),var(--silver) 60%,#9a9c9d);color:var(--black)}

.notice{position:absolute;left:24px;color:var(--white);font-size:8.6px;line-height:11px}

/* front card */
.c1 .lockup{left:12px;top:14px;gap:6px}
.c1 .lockup .dot{width:26px;height:26px}
.c1 .lockup .name .top{font-size:21px}
.c1 .lockup .name .sub{font-size:9px}
.c1 .person{position:absolute;right:14px;top:18px;font-size:9.5px;font-weight:600;color:var(--ink)}
.c1 .person span{color:var(--green);margin:0 3px}
.c1 .person small{font-size:8px;font-weight:600}
.c1 .rule{position:absolute;left:100px;right:10px;top:40px;height:1px;background:linear-gradient(90deg,transparent,#bbb)}
.c1 .address{position:absolute;left:60px;top:70px;font-size:9px;font-weight:600;line-height:11.5px}
.c1 .contact-col{position:absolute;left:0;top:102px;width:52px;height:68px;background:linear-gradient(90deg,transparent,#e4e4e4)}
.c1 .contacts{position:absolute;left:48px;top:107px;font-size:9px;font-weight:600;line-height:12.5px}
.c1 .contacts b{display:inline-block;width:12px;color:var(--green);font-weight:700}
.c1 .band{position:absolute;left:0;bottom:0;width:100%;height:30px;background:linear-gradient(180deg,var(--green-light),var(--green-dark));color:var(--white);font-size:9px;font-weight:700;padding:7px 0 0 100px}
</style>
</head>
<body>

<section class="panel panel-white">
  <div class="lockup lockup-lg on-white"><span class="dot"></span><span class="name"><span class="top">ORTELL</span><span class="sub">CONVEYANCING</span></span></div>
</section>

<section class="panel panel-black">
  <div class="lockup lockup-lg on-black"><span class="dot"></span><span class="name"><span class="top">ORTELL</span><span class="sub">CONVEYANCING</span></span></div>
</section>

<div class="lockup mono"><span class="dot"></span><span class="name"><span class="top">ORTELL</span><span class="sub">CONVEYANCING</span></span></div>

<div class="symbol-mark" role="img" aria-label="Brand symbol mark"></div>

<!-- Front -->
<article class="card c1">
  <div class="lockup on-white"><span class="dot"></span><span class="name"><span class="top">ORTELL</span><span class="sub">CONVEYANCING</span></span></div>
  <p class="person">Lena Marsh<span>|</span><small>Manager</small></p>
  <div class="rule"></div>
  <p class="address">48 Ashby Avenue<br>Westfield Park Victoria 3099</p>
  <div class="contact-col"></div>
  <p class="contacts"><b>T</b>(03) 9400 1122<br><b>F</b>(03) 9400 1133<br><b>E</b>ortellconveyancing@mailbox.com</p>
  <div class="band">www.ortellconveyancing.com</div>
</article>

<!-- Back: black / silver -->
<article class="card c2">
  <div class="bottom-green" style="height:82px"></div>
  <div class="top-black" style="height:115px"></div>
  <div class="lockup on-black" style="left:66px;top:34px"><span class="dot"></span><span class="name"><span class="top">ORTELL</span><span class="sub">CONVEYANCING</span></span></div>
  <div class="url-strip strip-silver" style="top:115px">www.ortellconveyancing.com</div>
  <p class="notice" style="top:140px">This firm holds professional indemnity insurance against civil liability<br>A solicitor is employed by this firm for all legal work.<br>Professional Indemnity.</p>
</article>

<!-- Back: green with black strip -->
<article class="card c3 fill-green">
  <div class="lockup on-green" style="left:80px;top:55px"><span class="dot"></span><span class="name"><span class="top">ORTELL</span><span class="sub">CONVEYANCING</span></span></div>
  <div class="url-strip strip-black" style="top:110px">www.ortellconveyancing.com</div>
  <p class="notice" style="top:145px">This firm holds professional indemnity insurance against civil liability<br>A solicitor is employed by this firm for all legal work.<br>Professional Indemnity.</p>
</article>

<!-- Back: black / black strip -->
<article class="card c4">
  <div class="bottom-green" style="height:90px"></div>
  <div class="top-black" style="height:109px"></div>
  <div class="lockup on-black" style="left:66px;top:32px"><span class="dot"></span><span class="name"><span class="top">ORTELL</span><span class="sub">CONVEYANCING</span></span></div>
  <div class="url-strip strip-black lime" style="top:109px">www.ortellconveyancing.com</div>
  <p class="notice" style="top:140px">This firm holds professional indemnity insurance against civil liability<br>A solicitor is employed by this firm for all legal work.<br>Professional Indemnity.</p>
</article>

<!-- Back: plain green -->
<article class="card c5 fill-green">
  <div class="lockup on-green" style="left:66px;top:44px"><span class="dot"></span><span class="name"><span class="top">ORTELL</span><span class="sub">CONVEYANCING</span></span></div>
  <p class="notice" style="top:135px">This firm holds professional indemnity insurance against civil liability<br>A solicitor is employed by this firm for all legal work.<br>Professional Indemnity.</p>
</article>

<!-- Back: green with lower strip -->
<article class="card c6 fill-green">
  <div class="lockup on-green" style="left:80px;top:42px"><span class="dot"></span><span class="name"><span class="top">ORTELL</span><span class="sub">CONVEYANCING</span></span></div>
  <div class="url-strip strip-black" style="top:112px;padding-left:90px">www.ortellconveyancing.com</div>
  <p class="notice" style="top:143px">This firm holds professional indemnity insurance against civil liability<br>A solicitor is employed by this firm for all legal work.<br>Professional Indemnity.</p>
</article>

</body>
</html>
```